Asian simmer/ cooking sauce label

We are a established small gourmet condiment company with a range of products. This is a new product range of 6 simmer sauces that we would like a label designed that represents our brand but individualizes the new range.
the label should have a upmarket authentic feel and represent Asian cooking done in a home made kitchen
There will be six varieties it they will al have the same generic design only the product details will change

Our current range can be viewed on our website www.plumwickpantry.com.au

Butter Chicken has been uploaded. it is one of the products that will be used with the new label
I have uploaded a drinking chocolate label we use that has a black pattern

Target Market(s)

gourmet food shops, gifts stores

Colors

Designer to choose colors to be used in the design.

Requirements
Must have
• the labels needs to include product name. product description, ingredients, weight, nutritional panel, manufactures details and be a sized to suit jars which I will supply
• label size aprox 200mm long x 70mm high
Nice to have
• We prefer warm colours, gold, and black
• our brand name and logo
Should not have
• surprise me

```html
<!DOCTYPE html>
<html lang="en">
<head>
<meta charset="utf-8">
<title>Simmer Sauce – Butter Chicken Label</title>
<link href="https://fonts.googleapis.com/css2?family=Jost:wght@300;400;500&family=Cinzel:wght@700&family=Kaushan+Script&family=Arimo:wght@400;700&family=Archivo+Black&display=swap" rel="stylesheet">
<style>
  :root{
    --stage:#4a4a4a;
    --label-dark:#0b0908;
    --label-brown:#2b231d;
    --gold:#b8975a;
    --gold-light:#c9a86b;
    --white:#ffffff;
    --ink:#000000;
  }
  *{box-sizing:border-box;margin:0;padding:0}
  html,body{width:1200px;height:1200px;overflow:hidden;background:var(--stage)}
  .label{
    position:absolute;left:63px;top:445px;width:1074px;height:309px;
    color:var(--gold);font-family:"Jost",sans-serif;
  }
  .label-pattern{
    position:absolute;inset:0;
    background:radial-gradient(ellipse at 50% 50%,var(--label-brown) 0%,#171310 55%,var(--label-dark) 100%);
  }
  .description{
    position:absolute;left:40px;top:30px;width:274px;
    font-weight:300;font-size:13.4px;line-height:18px;text-align:justify;
  }
  .ingredients{position:absolute;left:40px;top:128px;width:274px}
  .ingredients h2{
    font-weight:400;font-size:14px;letter-spacing:.4px;color:var(--white);margin-bottom:1px;
  }
  .ingredients p{font-weight:300;font-size:13.4px;line-height:18px;text-align:justify}
  .net-weight{
    position:absolute;left:40px;top:236px;
    font-weight:500;font-size:21px;color:var(--white);
  }
  .brand{
    position:absolute;left:337px;top:92px;width:400px;
    display:flex;align-items:center;justify-content:center;gap:10px;
  }
  .brand-mark{width:14px;height:14px;background:var(--gold-light)}
  .brand-name{
    font-family:"Jost",sans-serif;font-weight:500;font-size:24px;line-height:30px;
    color:var(--gold-light);
  }
  .product-range{
    position:absolute;left:337px;top:172px;width:400px;text-align:center;
    font-family:"Cinzel",serif;font-weight:700;font-size:40px;letter-spacing:1px;
    color:var(--gold);
  }
  .product-name{
    position:absolute;left:337px;top:220px;width:400px;text-align:center;
    font-family:"Kaushan Script",cursive;font-size:44px;color:var(--white);
  }
  .nutrition{
    position:absolute;left:745px;top:29px;width:173px;height:240px;
    background:var(--white);border:2px solid var(--white);outline:1px solid var(--ink);outline-offset:-4px;
    padding:5px 7px;color:var(--ink);font-family:"Arimo",sans-serif;font-size:7.4px;line-height:10.3px;
  }
  .nutrition h3{font-family:"Archivo Black",sans-serif;font-weight:400;font-size:17px;line-height:20px;letter-spacing:-.2px}
  .nutrition .row{display:flex;justify-content:space-between;border-top:.6px solid var(--ink)}
  .nutrition .thick{border-top:5px solid var(--ink)}
  .nutrition .mid{border-top:2.5px solid var(--ink)}
  .nutrition .sub{padding-left:9px}
  .nutrition b{font-weight:700}
  .nutrition .tiny{font-size:6.2px;font-weight:700}
  .nutrition .right{justify-content:flex-end}
  .manufacturer{
    position:absolute;left:940px;top:72px;height:198px;
    writing-mode:vertical-rl;transform:rotate(180deg);
    font-style:normal;font-weight:300;font-size:11.5px;line-height:16.5px;color:var(--gold);
  }
  .manufacturer .heading{font-weight:500;color:var(--white);letter-spacing:.4px}
  .manufacturer .company{font-weight:500}
</style>
</head>
<body>
  <section class="label">
    <div class="label-pattern" role="img" aria-label="Dark background with a faint gold geometric pattern"></div>

    <p class="description">Butter Chicken Simmer Sauce is an easy and tasty meal. Butter Chicken is a classic Indian dish. It has rich aromatic flavours without heat making it a great dish for the whole family.</p>

    <div class="ingredients">
      <h2>INGREDIENTS</h2>
      <p>Tomato, onions, garlic, ginger, tamarind, almond, ghee, salt, sugar, spice. CONTAINS NUTS &amp; DAIRY. May contain traces of gluten.</p>
    </div>

    <p class="net-weight">375 gms net</p>

    <div class="brand">
      <span class="brand-mark"></span>
      <p class="brand-name">Hollins Larder</p>
    </div>

    <h1 class="product-range">Simmer Sauce</h1>
    <p class="product-name">Butter Chicken</p>

    <div class="nutrition">
      <h3>Nutrition Facts</h3>
      <div>Serving Size 310 g</div>
      <div class="row thick tiny">Amount Per Serving</div>
      <div class="row"><span><b>Calories</b> 402</span><span>Calories from Fat 210</span></div>
      <div class="row mid right tiny">% Daily Value*</div>
      <div class="row"><span><b>Total Fat</b> 23.4g</span><b>36%</b></div>
      <div class="row sub"><span>Saturated Fat 9.3g</span><b>47%</b></div>
      <div class="row sub"><span><i>Trans</i> Fat 0.0g</span></div>
      <div class="row"><span><b>Cholesterol</b> 193mg</span><b>64%</b></div>
      <div class="row"><span><b>Sodium</b> 928mg</span><b>39%</b></div>
      <div class="row"><span><b>Potassium</b> 252mg</span><b>7%</b></div>
      <div class="row"><span><b>Total Carbohydrates</b> 9.8g</span><b>3%</b></div>
      <div class="row sub"><span>Dietary Fiber 0.9g</span><b>4%</b></div>
      <div class="row sub"><span>Sugars 6.5g</span></div>
      <div class="row"><span><b>Protein</b> 39.8g</span></div>
      <div class="row thick"><span>Vitamin A 16%</span><span>•</span><span>Vitamin C 15%</span></div>
      <div class="row" style="border-top:0"><span>Calcium 9%</span><span>•</span><span>Iron 15%</span></div>
      <div class="row mid"><b>Nutrition Grade C-</b></div>
      <div class="row">* Based on a 2000 calorie diet</div>
    </div>

    <address class="manufacturer">
      <span class="heading">MANUFACTURED BY</span><br>
      <span class="company">The Plumwick Kitchen</span><br>
      Wattle Mill Road<br>
      Kenmore NSW 2580 • Australia<br>
      phone: 02 5550 1234<br>
      email: hello@plumwickpantry.com.au
    </address>
  </section>
</body>
</html>
```